Vision Board Class Design needed

Hello, I need a business card design for a new Company based in Mount Harwood, Eastvale, Australia. The Company provides a training Class with approx. 5 guests. They learn how to choose and create positive things in their life. It is based on the principal of the Law of Attraction. Each guest receives a large coloured cardboard and magazines, affirmations to choose ideas to help create their new exciting life - all pasted onto a "Vision Board" which will be seen by them every day and help to clarify the vision and attract abundance, happiness & positivity into their lives. I would like to see designs with bright, happy colours - perhaps rainbows - anything that represents a new life and appears refreshing.
Many thanks.

Industry/Entity Type

Training

Contact Information for Business Card

Bright Horizon
Delia
Mobile 0473 206-558

Logo Text

Bright Horizon

Logo styles of interest
Abstract Logo
Requirements
Must have
• Happy, Bright colours!

```html
<!DOCTYPE html>
<html lang="en">
<head>
<meta charset="utf-8">
<title>Bright Horizon Delia – Business Card</title>
<link rel="stylesheet" href="https://fonts.googleapis.com/css2?family=Source+Code+Pro:wght@700&display=swap">
<style>
  :root {
    --backdrop: #161614;
    --text-yellow: #ffff00;
    --magenta: #ff00cc;
    --violet: #7a00a8;
    --navy: #000080;
    --blue: #0050c8;
    --cyan: #00ffff;
    --teal: #00c8a0;
    --green: #00b030;
    --lime: #80dc10;
    --yellow: #ffff00;
    --orange: #ff7800;
    --red: #ff0000;
  }
  html, body {
    margin: 0;
    padding: 0;
    overflow: hidden;
    background: var(--backdrop);
  }
  .card {
    position: relative;
    width: 1200px;
    height: 800px;
    overflow: hidden;
    background: var(--backdrop);
    font-family: "Source Code Pro", "Consolas", monospace;
  }
  .rainbow-oval {
    position: absolute;
    inset: 0;
  }
  .card-line {
    position: absolute;
    left: 0;
    width: 100%;
    margin: 0;
    text-align: center;
    color: var(--text-yellow);
    font-weight: 700;
    font-size: 45px;
    line-height: 1;
    white-space: nowrap;
  }
  .brand-name { top: 46px;  left: -17px; }
  .location   { top: 385px; left: 7px; }
  .contact    { top: 724px; left: -20px; }
</style>
</head>
<body>
  <div class="card">
    <svg class="rainbow-oval" width="1200" height="800" viewBox="0 0 1200 800" aria-hidden="true">
      <defs>
        <linearGradient id="rainbow" x1="0" y1="0" x2="0" y2="800" gradientUnits="userSpaceOnUse">
          <stop offset="0.07" stop-color="var(--magenta)"/>
          <stop offset="0.16" stop-color="var(--violet)"/>
          <stop offset="0.24" stop-color="var(--navy)"/>
          <stop offset="0.31" stop-color="var(--blue)"/>
          <stop offset="0.39" stop-color="var(--cyan)"/>
          <stop offset="0.46" stop-color="var(--teal)"/>
          <stop offset="0.55" stop-color="var(--green)"/>
          <stop offset="0.65" stop-color="var(--lime)"/>
          <stop offset="0.77" stop-color="var(--yellow)"/>
          <stop offset="0.87" stop-color="var(--orange)"/>
          <stop offset="0.96" stop-color="var(--red)"/>
        </linearGradient>
      </defs>
      <ellipse cx="600" cy="400" rx="627" ry="460" fill="url(#rainbow)"/>
    </svg>
    <p class="card-line brand-name">Bright Horizon Delia</p>
    <p class="card-line location">Mount Harwood, Eastvale, Australia</p>
    <p class="card-line contact">Mobile 0473 206-558</p>
  </div>
</body>
</html>
```